Infographics for Quorvel reports

Quorvel report is a summary of software developer skills.

Main purpose of our reports is to provide quick and easy insight into skill set of tested individual.
Our mission is to help talents to stand out.

Our target market is a male between 25-40, bit of a nerd, who likes technology and computer games.
The report should communicate quality and trust.

Report should fit on one A4 page and contain the following
1. Company logo - provided with the brief

2. Information about tested developer:
- Photo of developer
- Full name
- Location
- Email

3. How he or she compares against the average Software Developer:
- Collaboration ranking (0-100)
- Skills ranking by languages (up to 10 languages)

4. Total ranking - Number 1-100% which should stand out as a quick reference

We would like to included some sort of stamp of approval on the report.
The stamp would contain the overall score of a developer (The Total ranking from point 4.) .

As an option we were considering to use some sort of categorisation for the total ranking.
Here are examples of Quorvel categories:
Wizard of Quorvel for ranking between 90% – 100%
Scholar of Quorvel for ranking between 80% - 89%
Knight of Quorvel for ranking between 70% - 79%
Warrior of Quorvel for ranking between 60% - 69%
Rebel of Quorvel unknown or under 60%

Developer would belong to one of the categories depending on their Total ranking.

We are not very fixed on category names. We would be happy to consider any other option.

Here are some example data for the report:

The average Software Developer ranking is 50%.

Tested Developer:
Photo
Full name: Mark Tester
Location: Sydney, Australia
Email: mark.tester@mailvex.com

Collaboration ranking: 95%

Skills:
Language: C++
Number of Open Source Projects: 5
Ranking: 91%

Language: Javascript
Number of Open Source Projects: 3
Ranking: 81%

Language: Python
Number of Open Source Projects: 1
Ranking: 31%

Language: Ruby
Number of Open Source Projects: 2
Ranking: 25%

Language: C#
Ranking: 85%

Language: Java
Ranking: 75%

Total Ranking: 75% - Knight of Quorvel

Thank you!

```html
<!DOCTYPE html>
<html lang="en">
<head>
<meta charset="utf-8">
<title>Quorvel Report – Mark Tester</title>
<link href="https://fonts.googleapis.com/css2?family=Montserrat:wght@500;600;700;800&family=Roboto:wght@300;400&display=swap" rel="stylesheet">
<style>
  :root {
    --ink: #111111;
    --purple: #8e2b73;
    --grey-band: #d1d2d4;
    --track: #d6d6d6;
    --paper: #ffffff;
    --rule: #9a9a9a;
    --faint: #f7f2f5;
  }
  * { box-sizing: border-box; margin: 0; padding: 0; }
  html, body { width: 850px; height: 1200px; overflow: hidden; background: var(--paper); }
  .report {
    position: relative; width: 850px; height: 1200px; overflow: hidden;
    background: var(--paper); font-family: "Roboto", sans-serif; color: var(--ink);
  }

  /* top bar */
  .topbar { position: absolute; left: 0; top: 0; width: 850px; height: 84px; background: var(--ink); z-index: 2; }
  .report-title {
    position: absolute; left: 34px; top: 18px; color: var(--paper);
    font-family: "Montserrat", sans-serif; font-weight: 800; font-size: 19px; letter-spacing: 1px;
  }
  .report-note {
    position: absolute; left: 34px; top: 44px; color: var(--paper);
    font-family: "Montserrat", sans-serif; font-weight: 600; font-size: 10px;
  }
  .brand { position: absolute; right: 36px; top: 22px; display: flex; align-items: center; gap: 10px; }
  .brand-square { width: 36px; height: 36px; background: var(--purple); }
  .brand-name { font-family: "Montserrat", sans-serif; font-weight: 700; font-size: 32px; color: var(--paper); line-height: 1; }

  /* profile */
  .profile { position: absolute; left: 0; top: 84px; width: 850px; height: 238px; background: var(--grey-band); z-index: 2; }
  .photo-frame {
    position: absolute; left: 34px; top: 26px; width: 168px; height: 168px;
    border: 8px solid var(--ink); border-radius: 28px; background: var(--paper); overflow: hidden;
  }
  .photo { position: absolute; inset: 8px; border-radius: 18px; background: linear-gradient(180deg, #f4eef2 0%, #b76ca2 55%, var(--purple) 100%); }
  .label-tested { position: absolute; left: 250px; top: 40px; font-family: "Montserrat", sans-serif; font-weight: 500; font-size: 18px; }
  .dev-name { position: absolute; left: 248px; top: 58px; font-family: "Montserrat", sans-serif; font-weight: 800; font-size: 52px; letter-spacing: -0.5px; line-height: 1.1; }
  .contact { position: absolute; top: 124px; display: flex; align-items: center; gap: 9px; font-size: 17px; }
  .contact-location { left: 246px; }
  .contact-email { left: 456px; }
  .collab { position: absolute; left: 254px; top: 164px; font-family: "Montserrat", sans-serif; font-weight: 500; font-size: 18px; }

  /* skills band */
  .skills-band {
    position: absolute; left: 0; top: 322px; width: 850px; height: 64px; background: var(--purple);
    color: var(--paper); text-align: center; font-family: "Montserrat", sans-serif; font-weight: 800;
    font-size: 36px; line-height: 64px; z-index: 2;
  }
  .notch { position: absolute; width: 0; height: 0; border-left: 14px solid transparent; border-right: 14px solid transparent; z-index: 3; }
  .notch-up-purple { left: 103px; top: 308px; border-bottom: 14px solid var(--purple); }
  .notch-up-white { left: 103px; top: 372px; border-bottom: 14px solid var(--paper); }
  .notch-up-black { left: 103px; top: 1168px; border-bottom: 14px solid var(--ink); }

  /* faint backdrop, kept inside the skills area */
  .skills-backdrop { position: absolute; left: 0; top: 386px; width: 850px; height: 796px; overflow: hidden; z-index: 0; }
  .backdrop-shape { position: absolute; width: 260px; height: 260px; background: var(--faint); transform: rotate(45deg); }

  /* skill cards */
  .skill { position: absolute; width: 300px; height: 140px; z-index: 1; }
  .skill-diamond {
    position: absolute; left: 22px; top: 27px; width: 76px; height: 76px;
    background: var(--purple); border-radius: 10px; transform: rotate(45deg);
  }
  .skill-name {
    position: absolute; left: 0; top: 50px; width: 120px; text-align: center; color: var(--paper);
    font-family: "Montserrat", sans-serif; font-weight: 700; font-size: 23px; line-height: 30px;
  }
  .stats { position: absolute; left: 147px; top: 0; width: 138px; }
  .stat-row { position: absolute; left: 0; width: 138px; border-bottom: 1px solid var(--rule); }
  .stat-projects { top: 0; height: 28px; }
  .stat-rank { top: 62px; height: 47px; }
  .project-dot { position: absolute; left: 0; top: 0; width: 28px; height: 28px; border-radius: 50%; background: var(--purple); }
  .project-count { position: absolute; right: 0; bottom: -3px; font-weight: 300; font-size: 32px; line-height: 1; }
  .rank-ring { position: absolute; left: 0; top: 10px; }
  .rank-value { position: absolute; right: 0; bottom: -4px; font-weight: 300; font-size: 42px; line-height: 1; }
  .stat-caption { position: absolute; left: 0; font-size: 13px; }
  .caption-projects { top: 31px; }
  .caption-rank { top: 112px; }

  /* total badge */
  .total-badge { position: absolute; left: 315px; top: 1010px; width: 220px; height: 150px; z-index: 1; }
  .stamp {
    position: absolute; left: 5px; top: 80px; width: 212px; height: 44px; background: var(--purple);
    transform: rotate(-8deg); display: flex; align-items: center; gap: 10px; padding-left: 16px;
    outline: 2px dashed rgba(255,255,255,0.8); outline-offset: -6px;
  }
  .stamp-dot { width: 18px; height: 18px; border-radius: 50%; background: var(--paper); flex: none; }
  .stamp-text { color: var(--paper); font-family: "Montserrat", sans-serif; font-weight: 700; font-size: 15px; white-space: nowrap; }

  .bottombar { position: absolute; left: 0; top: 1182px; width: 850px; height: 18px; background: var(--ink); z-index: 2; }
</style>
</head>
<body>
<main class="report">
  <header class="topbar">
    <div class="report-title">QUORVEL REPORT</div>
    <div class="report-note">* The average Software Developer ranking is 50%.</div>
    <div class="brand"><span class="brand-square"></span><span class="brand-name">Quorvel</span></div>
  </header>

  <section class="profile">
    <div class="photo-frame"><div class="photo" role="img" aria-label="Portrait photo of the tested developer"></div></div>
    <div class="label-tested">Tested Developer:</div>
    <h1 class="dev-name">Mark Tester</h1>
    <div class="contact contact-location">
      <svg width="16" height="22" viewBox="0 0 16 22" aria-hidden="true"><path d="M8 0C3.6 0 0 3.5 0 7.9 0 13.5 8 22 8 22s8-8.5 8-14.1C16 3.5 12.4 0 8 0zm0 11a3.2 3.2 0 1 1 0-6.4A3.2 3.2 0 0 1 8 11z" fill="#111"/></svg>
      <span>Sydney, Australia</span>
    </div>
    <div class="contact contact-email">
      <svg width="26" height="18" viewBox="0 0 26 18" aria-hidden="true"><rect x="0" y="0" width="26" height="18" fill="#111"/><path d="M1 1l12 9 12-9" fill="none" stroke="#d1d2d4" stroke-width="2"/></svg>
      <span>mark.tester@mailvex.com</span>
    </div>
    <div class="collab">Collaboration Ranking: 95%</div>
  </section>

  <div class="notch notch-up-purple"></div>
  <h2 class="skills-band">SKILLS</h2>
  <div class="notch notch-up-white"></div>

  <div class="skills-backdrop" aria-hidden="true">
    <div class="backdrop-shape" style="left:140px;top:-150px;"></div>
    <div class="backdrop-shape" style="left:700px;top:420px;"></div>
  </div>

  <div class="skill" style="left:67px;top:451px;">
    <div class="skill-diamond"></div><div class="skill-name">.cpp</div>
    <div class="stats">
      <div class="stat-row stat-projects"><span class="project-dot"></span><span class="project-count">5</span></div>
      <div class="stat-caption caption-projects">Open Source Projects</div>
      <div class="stat-row stat-rank">
        <svg class="rank-ring" width="34" height="34" viewBox="0 0 34 34" aria-hidden="true"><circle cx="17" cy="17" r="13" fill="none" stroke="var(--track)" stroke-width="6"/><circle cx="17" cy="17" r="13" fill="none" stroke="var(--purple)" stroke-width="6" pathLength="100" stroke-dasharray="91 100" transform="rotate(-90 17 17)"/></svg>
        <span class="rank-value">91%</span>
      </div>
      <div class="stat-caption caption-rank">Ranking</div>
    </div>
  </div>

  <div class="skill" style="left:470px;top:451px;">
    <div class="skill-diamond"></div><div class="skill-name">.js</div>
    <div class="stats">
      <div class="stat-row stat-projects"><span class="project-dot"></span><span class="project-count">3</span></div>
      <div class="stat-caption caption-projects">Open Source Projects</div>
      <div class="stat-row stat-rank">
        <svg class="rank-ring" width="34" height="34" viewBox="0 0 34 34" aria-hidden="true"><circle cx="17" cy="17" r="13" fill="none" stroke="var(--track)" stroke-width="6"/><circle cx="17" cy="17" r="13" fill="none" stroke="var(--purple)" stroke-width="6" pathLength="100" stroke-dasharray="81 100" transform="rotate(-90 17 17)"/></svg>
        <span class="rank-value">81%</span>
      </div>
      <div class="stat-caption caption-rank">Ranking</div>
    </div>
  </div>

  <div class="skill" style="left:67px;top:653px;">
    <div class="skill-diamond"></div><div class="skill-name">.py</div>
    <div class="stats">
      <div class="stat-row stat-projects"><span class="project-dot"></span><span class="project-count">1</span></div>
      <div class="stat-caption caption-projects">Open Source Projects</div>
      <div class="stat-row stat-rank">
        <svg class="rank-ring" width="34" height="34" viewBox="0 0 34 34" aria-hidden="true"><circle cx="17" cy="17" r="13" fill="none" stroke="var(--track)" stroke-width="6"/><circle cx="17" cy="17" r="13" fill="none" stroke="var(--purple)" stroke-width="6" pathLength="100" stroke-dasharray="31 100" transform="rotate(-90 17 17)"/></svg>
        <span class="rank-value">31%</span>
      </div>
      <div class="stat-caption caption-rank">Ranking</div>
    </div>
  </div>

  <div class="skill" style="left:470px;top:653px;">
    <div class="skill-diamond"></div><div class="skill-name">.rb</div>
    <div class="stats">
      <div class="stat-row stat-projects"><span class="project-dot"></span><span class="project-count">2</span></div>
      <div class="stat-caption caption-projects">Open Source Projects</div>
      <div class="stat-row stat-rank">
        <svg class="rank-ring" width="34" height="34" viewBox="0 0 34 34" aria-hidden="true"><circle cx="17" cy="17" r="13" fill="none" stroke="var(--track)" stroke-width="6"/><circle cx="17" cy="17" r="13" fill="none" stroke="var(--purple)" stroke-width="6" pathLength="100" stroke-dasharray="25 100" transform="rotate(-90 17 17)"/></svg>
        <span class="rank-value">25%</span>
      </div>
      <div class="stat-caption caption-rank">Ranking</div>
    </div>
  </div>

  <div class="skill" style="left:67px;top:857px;">
    <div class="skill-diamond"></div><div class="skill-name">.cs</div>
    <div class="stats">
      <div class="stat-row stat-projects"><span class="project-dot"></span><span class="project-count">3</span></div>
      <div class="stat-caption caption-projects">Open Source Projects</div>
      <div class="stat-row stat-rank">
        <svg class="rank-ring" width="34" height="34" viewBox="0 0 34 34" aria-hidden="true"><circle cx="17" cy="17" r="13" fill="none" stroke="var(--track)" stroke-width="6"/><circle cx="17" cy="17" r="13" fill="none" stroke="var(--purple)" stroke-width="6" pathLength="100" stroke-dasharray="85 100" transform="rotate(-90 17 17)"/></svg>
        <span class="rank-value">85%</span>
      </div>
      <div class="stat-caption caption-rank">Ranking</div>
    </div>
  </div>

  <div class="skill" style="left:470px;top:857px;">
    <div class="skill-diamond"></div><div class="skill-name">.java</div>
    <div class="stats">
      <div class="stat-row stat-projects"><span class="project-dot"></span><span class="project-count">5</span></div>
      <div class="stat-caption caption-projects">Open Source Projects</div>
      <div class="stat-row stat-rank">
        <svg class="rank-ring" width="34" height="34" viewBox="0 0 34 34" aria-hidden="true"><circle cx="17" cy="17" r="13" fill="none" stroke="var(--track)" stroke-width="6"/><circle cx="17" cy="17" r="13" fill="none" stroke="var(--purple)" stroke-width="6" pathLength="100" stroke-dasharray="75 100" transform="rotate(-90 17 17)"/></svg>
        <span class="rank-value">75%</span>
      </div>
      <div class="stat-caption caption-rank">Ranking</div>
    </div>
  </div>

  <div class="total-badge">
    <svg width="220" height="110" viewBox="0 0 220 110" aria-hidden="true">
      <circle cx="110" cy="55" r="52" fill="#111"/>
      <circle cx="110" cy="55" r="40" fill="#fff"/>
      <circle cx="110" cy="55" r="34" fill="none" stroke="#111" stroke-width="3"/>
      <g fill="#fff">
        <circle cx="80" cy="24" r="2.5"/><circle cx="90" cy="15" r="2.5"/><circle cx="103" cy="10" r="2.5"/>
        <circle cx="117" cy="10" r="2.5"/><circle cx="130" cy="15" r="2.5"/><circle cx="140" cy="24" r="2.5"/>
      </g>
      <text x="110" y="67" text-anchor="middle" font-family="Montserrat, sans-serif" font-weight="800" font-size="32" fill="#111">75</text>
    </svg>
    <div class="stamp"><span class="stamp-dot"></span><span class="stamp-text">Knight of Quorvel</span></div>
  </div>

  <div class="notch notch-up-black"></div>
  <footer class="bottombar"></footer>
</main>
</body>
</html>
```